New Dental Office Needs an Attractive and user friendly Website Designed

I need a website for a new dental office. The Name is Larkhaven Dentistry. I would like a Modern design with a user friendly interface and usability.
I would like a landing page, a page that lists the services we offer: Cosmetic Dentistry, Implants, Dental Hygiene, Emergency Services, Restorations, Dentures
Target Market(s)
Mid to upper class
Industry/Entity Type
Dentistry
Coding
Coded - Design and coding required
Number of Pages Required
1 page
Requirements
Must have
- Landing page that has a scheduling option, Procedures, operating hours, and contact us info
Nice to have
- Appealing design, Soft comforting colors. Easy to navigate page, Modern and professional.

```html
<!DOCTYPE html>
<html lang="en">
<head>
<meta charset="utf-8">
<title>Larkhaven Dentistry</title>
<link href="https://fonts.googleapis.com/css2?family=Arvo:wght@400;700&family=Lato:wght@400;700;900&display=swap" rel="stylesheet">
<style>
:root{
  --blue:#1b6a99;
  --navy:#1f4e79;
  --sky:#5ec0ec;
  --ink:#222;
  --muted:#555;
  --grey:#efefef;
  --dark:#1c1c1c;
  --white:#fff;
}
*{box-sizing:border-box;margin:0;padding:0}
html,body{width:1200px;height:5146px;overflow:hidden}
body{font-family:"Lato",sans-serif;color:var(--ink);background:var(--white);position:relative}
section,header,footer{position:absolute;left:0;width:1200px;overflow:hidden}
.abs{position:absolute}
.btn{position:absolute;display:inline-block;font-weight:900;font-size:15px;letter-spacing:.5px;color:var(--white);padding:11px 16px}
.btn-sky{background:var(--sky)}
.btn-navy{background:var(--navy)}
p.body{font-size:13.5px;line-height:25px;color:var(--ink)}
/* header */
.site-header{top:0;height:104px;background:var(--white)}
.brand{position:absolute;left:108px;top:18px;font-family:"Arvo",serif;font-size:30px;color:var(--ink);line-height:34px;width:220px;text-align:center}
.brand small{display:block;font-size:16px;letter-spacing:6px;line-height:22px}
.topbar{position:absolute;left:410px;top:0;width:790px;height:48px;background:var(--blue);clip-path:polygon(0 0,100% 0,100% 100%,36px 100%)}
.topbar span{position:absolute;top:15px;color:var(--white);font-size:15px;font-weight:700;white-space:nowrap}
.topbar i{display:inline-block;width:24px;height:24px;border-radius:50%;background:var(--sky);vertical-align:middle;margin-right:8px;margin-top:-4px}
.nav{position:absolute;top:58px;left:448px;height:40px;display:flex;gap:30px;font-size:15px;align-items:center}
.nav a{color:var(--ink);text-decoration:none;white-space:nowrap}
.nav a.active{color:var(--blue);font-weight:700;border-bottom:2px solid var(--blue);padding-bottom:2px}
.nav a.nav-book{background:var(--sky);color:var(--white);padding:10px 16px;font-weight:900;font-size:14px}
/* hero */
.hero{top:104px;height:600px;background:linear-gradient(100deg,#5f7d3f 0%,#7c8f57 30%,#3f5e2e 60%,#2e4a24 100%)}
.hero h1{position:absolute;left:610px;top:180px;font-family:"Arvo",serif;font-size:60px;line-height:72px;color:var(--white);font-weight:700}
.hero p{position:absolute;left:610px;top:338px;width:480px;color:var(--white);font-size:14px;line-height:30px}
.arrow{position:absolute;width:36px;height:36px;border:2px solid var(--white);border-radius:50%}
/* welcome */
.welcome{top:704px;height:512px}
.welcome h2{position:absolute;left:110px;top:100px;font-family:"Arvo",serif;font-size:34px;line-height:44px}
.welcome h2 em{font-style:normal;color:var(--blue)}
.rule{position:absolute;height:3px;width:46px;background:var(--blue)}
.slant-img{position:absolute}
/* features */
.features{top:1216px;height:630px;background:linear-gradient(135deg,#f3f2f0,#e9e7e3 50%,#f4f3f1)}
.card{position:absolute;background:var(--white);box-shadow:0 2px 12px rgba(0,0,0,.12);width:468px;height:184px}
.card .ico{position:absolute;left:20px;top:26px;width:72px;height:62px;background:var(--blue)}
.card h3{position:absolute;left:118px;top:32px;font-family:"Arvo",serif;color:var(--blue);font-size:18px}
.card p{position:absolute;left:118px;top:64px;width:330px;font-size:13px;line-height:23px}
.card a{position:absolute;left:118px;top:142px;font-family:"Arvo",serif;color:var(--blue);font-size:13px;font-weight:700;text-decoration:underline}
/* procedures */
.procedures{top:1846px;height:696px;background:var(--blue)}
.procedures h2{position:absolute;top:100px;width:100%;text-align:center;font-family:"Arvo",serif;color:var(--white);font-size:32px}
.svc{position:absolute;top:186px;width:222px;height:394px;background:var(--white);text-align:center;overflow:hidden}
.svc .photo{height:170px}
.svc .badge{position:absolute;left:76px;top:134px;width:70px;height:70px;border-radius:50%;background:var(--blue);border:4px solid var(--white)}
.svc h3{position:absolute;left:0;top:226px;width:100%;font-size:13px;font-weight:900}
.svc p{position:absolute;top:254px;left:26px;width:170px;font-size:12.5px;line-height:22px}
.svc a{position:absolute;left:0;top:340px;width:100%;height:40px;line-height:40px;font-size:12.5px;font-weight:900;color:var(--navy)}
.svc.on a{top:350px;height:44px;line-height:44px;background:var(--sky);color:var(--white)}
/* hours */
.hours{top:2542px;height:518px}
.hours h2{position:absolute;left:680px;top:96px;font-family:"Arvo",serif;font-size:30px;color:var(--blue)}
.day{position:absolute;left:680px;width:400px;height:70px}
.day .tooth{position:absolute;left:0;top:0;width:50px;height:60px}
.day b{position:absolute;left:84px;top:4px;font-size:14px;font-weight:900}
.day span{position:absolute;left:86px;top:32px;font-size:14.5px;color:#333}
/* reviews */
.reviews{top:3060px;height:528px;background:var(--grey)}
.reviews h2{position:absolute;top:126px;width:100%;text-align:center;font-family:"Arvo",serif;font-size:30px}
.reviews h2 em{font-style:normal;color:var(--blue)}
.rev{position:absolute;top:208px;width:434px;height:232px;background:var(--white);border-radius:8px;box-shadow:0 2px 10px rgba(0,0,0,.1)}
.rev .avatar{position:absolute;left:32px;top:20px;width:70px;height:70px;border-radius:50%;background:linear-gradient(#8a8a8a,#4a4a4a)}
.rev b{position:absolute;left:136px;top:24px;font-size:15px}
.rev small{position:absolute;left:136px;top:52px;font-size:14px}
.rev .stars{position:absolute;left:124px;top:76px;color:#f2b705;font-size:14px;letter-spacing:1px}
.rev p{position:absolute;left:32px;top:110px;width:372px;font-size:12.5px;line-height:24px;color:#333}
/* booking */
.booking{top:3588px;height:512px;background:linear-gradient(90deg,#b7a48e 0%,#9a8066 45%,#6f5644 100%)}
.booking h2{position:absolute;left:108px;top:82px;font-family:"Arvo",serif;font-size:40px;line-height:56px;color:var(--white);font-weight:400}
.stat{position:absolute;left:110px;color:var(--white);font-size:18px}
.stat strong{font-size:28px;font-weight:900;margin:0 6px 0 14px}
.stat::before{content:"";position:absolute;left:0;top:12px;width:10px;height:10px;border-radius:50%;background:var(--white)}
/* request */
.request{top:4100px;height:700px}
.request h2{position:absolute;top:90px;width:100%;text-align:center;font-size:28px;font-weight:900;letter-spacing:.5px}
.request h3{position:absolute;left:136px;top:182px;font-size:20px;font-weight:900}
.field{position:absolute;left:136px;width:434px;border-bottom:1px solid #999;font-size:12.5px;padding:18px 0 0 12px;height:46px}
.contact-box{position:absolute;left:664px;top:190px;width:424px;height:440px;background:var(--blue);border-radius:14px}
.ci{position:absolute;left:36px;width:380px;color:var(--white)}
.ci i{position:absolute;left:0;top:6px;width:34px;height:34px;border-radius:50%;background:#3f9bd3}
.ci b{display:block;margin-left:54px;font-size:16px;font-weight:900;line-height:26px;letter-spacing:.5px}
.soc{position:absolute;top:402px;width:26px;height:26px;border-radius:50%;background:#4aa6dc}
/* footer */
.site-footer{top:4800px;height:346px;background:var(--dark);color:var(--white)}
.site-footer .flogo{position:absolute;top:96px;width:100%;text-align:center;font-family:"Arvo",serif;font-size:38px;line-height:44px}
.site-footer .flogo small{display:block;font-size:19px;letter-spacing:8px}
.fnav{position:absolute;top:202px;width:100%;display:flex;justify-content:center;gap:54px;font-size:15px}
.copy{position:absolute;top:266px;width:100%;text-align:center;font-size:13.5px}
</style>
</head>
<body>

<header class="site-header">
  <div class="brand">Larkhaven<small>DENTISTRY</small></div>
  <div class="topbar">
    <span style="left:104px"><i></i>PHONE: (555) 210-4800</span>
    <span style="left:360px"><i></i>EMAIL: info@larkhavendentistry.com</span>
  </div>
  <nav class="nav">
    <a class="active">Home</a><a>Treatments</a><a>About Us</a><a>Fees</a><a>Offers</a><a>Contact Us</a><a class="nav-book">BOOK NOW</a>
  </nav>
</header>

<section class="hero">
  <div class="abs" role="img" aria-label="Smiling young woman holding a clear aligner outdoors among trees" style="left:0;top:0;width:600px;height:600px;background:linear-gradient(90deg,#4d6a34,#8e8a5e 40%,#6a7a48)"></div>
  <h1>Healthy Smiles<br>Start Here.</h1>
  <p>Lorem ipsum dolor sit amet, consectetur adipiscing elit, sed do eiusmod tempor incididunt ut labore et dolore magna aliqua.</p>
  <span class="btn btn-sky" style="left:610px;top:418px;padding:13px 16px">SCHEDULE NOW</span>
  <span class="arrow" style="left:34px;top:282px"></span>
  <span class="arrow" style="left:1130px;top:282px"></span>
</section>

<section class="welcome">
  <h2><em>Welcome To</em><br>Larkhaven Dentistry</h2>
  <div class="rule" style="left:110px;top:200px"></div>
  <p class="body abs" style="left:110px;top:222px;width:490px">Lorem ipsum dolor sit amet, consectetur adipiscing elit, sed do eiusmod tempor incididunt ut labore et dolore magna aliqua. Ut enim ad minim veniam, quis nostrud exercitation ullamco laboris nisi ut aliquip ex ea commodo consequat. Duis aute irure dolor in reprehenderit in voluptate velit esse cillum dolore eu fugiat nulla pariatur.</p>
  <span class="btn btn-navy" style="left:110px;top:370px;font-size:13px">READ MORE</span>
  <div class="slant-img" role="img" aria-label="Dentist in blue gloves examining a smiling patient in the chair" style="left:552px;top:0;width:648px;height:512px;clip-path:polygon(30% 0,100% 0,60% 100%,0 100%);background:linear-gradient(135deg,#e6e1da,#b7c9d6 50%,#8fb2cc)"></div>
</section>

<section class="features">
  <div class="card" style="left:112px;top:106px"><div class="ico"></div><h3>Transparent Pricing</h3><p>Lorem ipsum dolor sit amet, consectetur adipiscing elit, sed do eiusmod tempor incididunt ut labore et dolore magna aliqua.</p><a>Read More</a></div>
  <div class="card" style="left:622px;top:106px"><div class="ico"></div><h3>3-year Guarantee</h3><p>Lorem ipsum dolor sit amet, consectetur adipiscing elit, sed do eiusmod tempor incididunt ut labore et dolore magna aliqua.</p><a>Read More</a></div>
  <div class="card" style="left:112px;top:330px"><div class="ico"></div><h3>Interest free finance</h3><p>Whilst we offer competitive prices, we understand you may prefer to spread the cost of your treatment over convenient monthly payments.</p><a>Read More</a></div>
  <div class="card" style="left:622px;top:330px"><div class="ico"></div><h3>Long Term Results</h3><p>Lorem ipsum dolor sit amet, consectetur adipiscing elit, sed do eiusmod tempor incididunt ut labore et dolore magna aliqua.</p><a>Read More</a></div>
  <div class="abs" style="left:550px;top:266px;width:100px;height:100px;border-radius:50%;background:var(--white);border:3px solid #bfe4f6"></div>
</section>

<section class="procedures">
  <h2>Procedures &amp; Services</h2>
  <div class="rule" style="left:576px;top:148px;background:var(--white)"></div>
  <div class="svc" style="left:112px"><div class="photo" role="img" aria-label="Woman with a bright smile at a dental check-up" style="background:linear-gradient(135deg,#e8ddd3,#c9b7a6)"></div><div class="badge"></div><h3>COSMETIC DENTISTRY</h3><p>Duis aute irure dolor in reprehenderit in voluptate fugiat nulla pariatur.</p><a>READ MORE</a></div>
  <div class="svc" style="left:364px"><div class="photo" role="img" aria-label="Dental implant model held by gloved hands" style="background:linear-gradient(135deg,#1f3f58,#3c6d8e)"></div><div class="badge"></div><h3>IMPLANTS</h3><p>Duis aute irure dolor in reprehenderit in voluptate fugiat nulla pariatur.</p><a>READ MORE</a></div>
  <div class="svc on" style="left:616px"><div class="photo" role="img" aria-label="Father and daughter brushing teeth together" style="background:linear-gradient(135deg,#d9c4ad,#8a6a52)"></div><div class="badge"></div><h3>DENTAL HYGIENE</h3><p>Duis aute irure dolor in reprehenderit in voluptate fugiat nulla pariatur.</p><a>READ MORE</a></div>
  <div class="svc" style="left:868px"><div class="photo" role="img" aria-label="Set of dentures on a blue background" style="background:linear-gradient(135deg,#6fa3c8,#c85a5a 60%,#e9e4de)"></div><div class="badge"></div><h3>DENTURES</h3><p>Duis aute irure dolor in reprehenderit in voluptate fugiat nulla pariatur.</p><a>READ MORE</a></div>
  <span class="arrow" style="left:40px;top:378px;width:28px;height:28px"></span>
  <span class="arrow" style="left:1132px;top:378px;width:28px;height:28px"></span>
</section>

<section class="hours">
  <div class="slant-img" role="img" aria-label="Smiling young girl during a dental check-up" style="left:0;top:0;width:655px;height:518px;clip-path:polygon(0 0,72% 0,100% 100%,0 100%);background:linear-gradient(135deg,#c9d8e2,#e8d6c8 45%,#5b8fb6)"></div>
  <h2>Operating Hours</h2>
  <div class="rule" style="left:680px;top:146px"></div>
  <div class="day" style="top:182px"><svg class="tooth" viewBox="0 0 50 60"><path d="M6 6 C14 0 20 6 25 6 C30 6 36 0 44 6 C50 14 44 30 42 44 C40 56 34 56 32 44 C30 36 20 36 18 44 C16 56 10 56 8 44 C6 30 0 14 6 6Z" fill="var(--blue)"/><circle cx="25" cy="24" r="8" fill="none" stroke="#fff" stroke-width="2"/></svg><b>MONDAY</b><span>9.00 AM TO 6.00 PM HOURS</span></div>
  <div class="day" style="top:276px"><svg class="tooth" viewBox="0 0 50 60"><path d="M6 6 C14 0 20 6 25 6 C30 6 36 0 44 6 C50 14 44 30 42 44 C40 56 34 56 32 44 C30 36 20 36 18 44 C16 56 10 56 8 44 C6 30 0 14 6 6Z" fill="var(--blue)"/><circle cx="25" cy="24" r="8" fill="none" stroke="#fff" stroke-width="2"/></svg><b>TUESDAY - WEDNESDAY</b><span>10.00 AM TO 7.00 PM HOURS</span></div>
  <div class="day" style="top:370px"><svg class="tooth" viewBox="0 0 50 60"><path d="M6 6 C14 0 20 6 25 6 C30 6 36 0 44 6 C50 14 44 30 42 44 C40 56 34 56 32 44 C30 36 20 36 18 44 C16 56 10 56 8 44 C6 30 0 14 6 6Z" fill="var(--blue)"/><circle cx="25" cy="24" r="8" fill="none" stroke="#fff" stroke-width="2"/></svg><b>THUSDAY - FRIDAY</b><span>10.00 AM TO 7.00 PM HOURS</span></div>
</section>

<section class="reviews">
  <h2><em>Patients</em> Reviews</h2>
  <div class="rev" style="left:142px"><div class="avatar" role="img" aria-label="Patient portrait"></div><b>Miss S</b><small>Treatment: Clear Aligners</small><span class="stars">★★★★★</span><p>Duis aute irure dolor in reprehenderit in voluptate velit esse cillum dolore eu fugiat nulla pariatur. Excepteur sint occaecat cupidatat non proident, sunt in culpa qui officia deserunt mollit anim id est laborum.</p></div>
  <div class="rev" style="left:634px"><div class="avatar" role="img" aria-label="Patient portrait"></div><b>Mr O</b><small>Treatment: Porcelain Veneers</small><span class="stars">★★★★★</span><p>Duis aute irure dolor in reprehenderit in voluptate velit esse cillum dolore eu fugiat nulla pariatur. Excepteur sint occaecat cupidatat non proident, sunt in culpa qui officia deserunt mollit anim id est laborum.</p></div>
  <svg class="abs" style="left:44px;top:290px" width="24" height="44" viewBox="0 0 24 44"><path d="M22 2 L2 22 L22 42" fill="none" stroke="#222" stroke-width="2.5"/></svg>
  <svg class="abs" style="left:1134px;top:290px" width="24" height="44" viewBox="0 0 24 44"><path d="M2 2 L22 22 L2 42" fill="none" stroke="#222" stroke-width="2.5"/></svg>
</section>

<section class="booking">
  <div class="abs" role="img" aria-label="Three generations of women smiling together on a sofa" style="left:560px;top:0;width:640px;height:512px;background:linear-gradient(90deg,rgba(150,120,95,0),#7a5a44 40%,#caa86a 80%,#8b6b52)"></div>
  <h2>Book Your<br>Appointment Today!</h2>
  <div class="stat" style="top:220px"><strong>6,000+</strong>Implants Placed</div>
  <div class="stat" style="top:272px"><strong>10,000+</strong>Smiles Transformed</div>
  <div class="stat" style="top:322px"><strong>11+</strong>Year Followup</div>
  <span class="btn btn-sky" style="left:110px;top:388px;font-size:16px">Schedule Now</span>
</section>

<section class="request">
  <h2>REQUEST AN APPOINTMENT</h2>
  <h3>CONTACT US</h3>
  <p class="abs" style="left:136px;top:220px;width:440px;font-size:13.5px;line-height:26px">Duis aute irure dolor in reprehenderit in voluptate velit esse cillum dolore eu fugiat nulla pariatur. Excepteur sint occaecat cupidatat non proident, sunt in mollit anim id est laborum.</p>
  <div class="field" style="top:308px">Full Name*</div>
  <div class="field" style="top:384px">Email Address*</div>
  <div class="field" style="top:460px">Message*</div>
  <span class="btn btn-navy" style="left:136px;top:546px;font-size:15px;padding:13px 26px">BOOK NOW</span>
  <div class="contact-box">
    <div class="ci" style="top:46px"><i></i><b>PHONE:<br>(555) 210-4800</b></div>
    <div class="ci" style="top:116px"><i></i><b>PHONE:<br>(555) 429-3160</b></div>
    <div class="ci" style="top:192px"><i></i><b>EMAIL:<br>hello@larkhavendentistry.com</b></div>
    <div class="ci" style="top:262px"><i></i><b>WEBSITE:<br>www.larkhavendentistry.com</b></div>
    <span class="soc" style="left:46px"></span><span class="soc" style="left:84px"></span><span class="soc" style="left:122px"></span><span class="soc" style="left:160px"></span>
  </div>
</section>

<footer class="site-footer">
  <div class="flogo">Larkhaven<small>DENTISTRY</small></div>
  <div class="fnav"><span>Home</span><span>Treatments</span><span>About Us</span><span>Fees</span><span>Offers</span><span>Contact Us</span></div>
  <div class="copy">Copyrights@2025.Company Name.All Rights Reserved</div>
</footer>

</body>
</html>
```